A online shop for solid wood need a Stationary design

A new online shop (in Austria and Germany) for solid wood and steel furniture (feldberg-formwerk) needs a Stationay design (letterhead, business card, envelope etc...). Dining tables, coffee tables, TV furniture and similar furniture will be sold. Everything will be custom made.

```html
<!DOCTYPE html>
<html lang="en">
<head>
<meta charset="utf-8">
<title>Feldberg Formwerk – Stationery</title>
<link href="https://fonts.googleapis.com/css2?family=Open+Sans:wght@400;600;700&family=Questrial&family=Tinos&display=swap" rel="stylesheet">
<style>
:root{
  --bg:#2b2b2b;
  --red:#d9180f;
  --red-deep:#c8120c;
  --orange:#ec6a14;
  --peach:#f7dcc4;
  --paper:#ffffff;
  --paper-shade:#f1f1f1;
  --ink:#1e1e1e;
  --grey:#8a8a8a;
  --ghost:rgba(0,0,0,0.045);
  --band:linear-gradient(90deg,var(--red-deep) 0%,var(--red) 18%,var(--orange) 55%,#f3a25e 80%,var(--peach) 100%);
}
*{box-sizing:border-box;margin:0;padding:0}
html,body{width:1200px;height:900px;overflow:hidden;background:var(--bg)}
.canvas{position:relative;width:1200px;height:900px;font-family:"Open Sans",sans-serif}
.project-title{position:absolute;right:45px;top:34px;font-family:"Questrial",sans-serif;font-size:46px;color:#fff;letter-spacing:-1px}

/* brand name lockup */
.brand{display:flex;align-items:center;gap:5px;color:var(--red);font-weight:700;text-transform:uppercase;line-height:1.05}
.brand-square{background:var(--red);flex:none}
.brand.light{color:#fff}
.brand.light .brand-square{background:#fff}

/* letterhead */
.letterhead{position:absolute;left:234px;top:225px;width:425px;height:550px;background:linear-gradient(180deg,var(--paper-shade) 0%,var(--paper) 8%);overflow:hidden;box-shadow:0 4px 12px rgba(0,0,0,.5)}
.letterhead .brand{position:absolute;left:57px;top:48px;font-size:13px}
.letterhead .brand-square{width:14px;height:14px}
.ghost-name{position:absolute;font-weight:700;color:var(--ghost);white-space:nowrap;letter-spacing:2px}
.letterhead .ghost-name{left:110px;top:455px;font-size:62px}
.letter{position:absolute;left:57px;top:125px;width:318px;font-family:"Tinos",serif;font-size:7.6px;line-height:9.2px;color:var(--ink)}
.recipient{display:flex;gap:14px;margin-bottom:19px}
.letter p{margin-bottom:9px}
.signature-area{width:95px;height:30px;background:linear-gradient(90deg,rgba(40,50,140,.18),rgba(40,50,140,.06));border-radius:3px;margin-top:-4px}
.footer-band{position:absolute;left:0;right:0;bottom:0;height:28px;background:var(--band);border-top:3px solid #111}
.footer-band span{position:absolute;left:57px;top:8px;font-size:5px;color:#fff}
.footer-band b{font-weight:700}

/* envelope */
.envelope{position:absolute;left:563px;top:177px;width:475px;height:275px}
.flap{position:absolute;left:5px;right:5px;top:0;height:68px;border-radius:8px 8px 0 0;overflow:hidden;transform:rotate(180deg);background:var(--paper)}
.flap-band{position:absolute;left:0;right:0;bottom:0;top:0;height:53px;background:var(--band);transform:scaleX(-1);border-bottom:2px solid #111}
.flap-url{position:absolute;left:0;right:0;bottom:3px;text-align:center;font-size:5px;color:#333;transform:translateX(-30px)}
.flap .brand{position:absolute;right:30px;top:17px;font-size:8px}
.flap .brand-square{width:10px;height:10px}
.flap-tagline{position:absolute;left:195px;top:11px;font-size:9px;line-height:10px;color:#fff;letter-spacing:1px}
.env-body{position:absolute;left:0;right:0;top:68px;bottom:0;background:var(--paper);overflow:hidden;box-shadow:0 4px 12px rgba(0,0,0,.5)}
.env-body .brand{position:absolute;left:28px;top:16px;font-size:12px}
.env-body .brand-square{width:13px;height:13px}
.env-body .ghost-name{left:185px;top:110px;font-size:54px}
.env-body .footer-band{height:30px}
.env-body .footer-band span{left:22px;top:10px}

/* business cards */
.card{position:absolute;width:172px;height:97px;border-radius:7px;overflow:hidden;box-shadow:0 3px 8px rgba(0,0,0,.55)}
.card-front{left:623px;top:495px;background:linear-gradient(100deg,var(--red-deep) 0%,var(--red) 30%,var(--orange) 65%,#f2a468 100%)}
.card-front .brand{position:absolute;left:22px;top:34px;font-size:8px}
.card-front .brand-square{width:9px;height:9px}
.card-tagline{position:absolute;left:85px;top:34px;font-size:9px;line-height:10px;color:#3a1608;letter-spacing:.6px}
.card-tagline .spaced{letter-spacing:4.3px}
.card-url{position:absolute;left:84px;top:84px;font-size:4.6px;color:#5b2008}
.card-back{left:757px;top:567px;height:98px;background:linear-gradient(180deg,#f7f7f7,var(--paper) 40%)}
.card-back .brand{position:absolute;left:18px;top:36px;font-size:7.5px}
.card-back .brand-square{width:9px;height:9px}
.card-person{position:absolute;left:90px;top:35px;color:var(--ink)}
.card-person .name{font-size:6px;font-weight:700}
.card-person .role{font-size:3.8px;margin-bottom:7px}
.card-person .contact{font-size:3.6px;line-height:4.8px}
.card-back .footer-band{height:22px;border-top-width:2px}
.card-back .footer-band span{left:11px;top:6px;font-size:4px}
</style>
</head>
<body>
<main class="canvas">
  <h1 class="project-title">Feldberg Formwerk</h1>

  <section class="letterhead">
    <div class="brand"><span class="brand-square"></span><span>Feldberg<br>Formwerk</span></div>
    <div class="ghost-name">FELDBERG</div>
    <div class="letter">
      <div class="recipient"><span>To:</span><span>Mr./Mrs. Customerand Partner<br>42 Orchard Street<br>Springfield<br>IL 62701</span></div>
      <p>Dear Customer,</p>
      <p>Lorem ipsum dolor sit amet, consetetur sadipscing elitr, sed diam nonumy eirmod tempor invidunt ut labore et dolore magna aliquyam erat, sed diam voluptua. At vero eos et accusam et justo duo dolores et ea rebum. Stet clita kasd gubergren, no sea takimata sanctus est Lorem ipsum dolor sit amet. Lorem ipsum dolor sit amet, consetetur sadipscing elitr, sed diam nonumy eirmod tempor invidunt ut labore et dolore magna aliquyam erat, sed diam voluptua. At vero eos et accusam et justo duo dolores et ea rebum. Stet clita kasd gubergren, no sea takimata sanctus est Lorem ipsum dolor sit amet. Lorem ipsum dolor sit amet, consetetur sadipscing elitr, sed diam nonumy eirmod tempor invidunt ut labore et dolore magna aliquyam erat, sed diam voluptua. At vero eos et accusam et justo duo dolores et ea rebum. Stet clita kasd gubergren, no sea takimata sanctus est Lorem ipsum dolor sit amet.</p>
      <p>Duis autem vel eum iriure dolor in hendrerit in vulputate velit esse molestie consequat, vel illum dolore eu feugiat nulla facilisis at vero eros et accumsan et iusto odio dignissim qui blandit praesent luptatum zzril delenit augue duis dolore te feugait nulla facilisi. Lorem ipsum dolor sit amet, consectetuer adipiscing elit, sed diam nonummy nibh euismod tincidunt ut laoreet dolore magna aliquam erat volutpat.</p>
      <p>Nam liber tempor cum soluta nobis eleifend option congue nihil imperdiet doming id quod mazim placerat facer possim assum. Lorem ipsum dolor sit amet, consectetuer adipiscing elit, sed diam nonummy nibh euismod tincidunt ut laoreet dolore magna aliquam erat volutpat. Ut wisi enim ad minim veniam, quis nostrud exerci tation ullamcorper suscipit lobortis nisl ut aliquip ex ea commodo consequat.</p>
      <p style="margin-bottom:4px">Sincerely,</p>
      <div class="signature-area" role="img" aria-label="Handwritten signature of Lena Hartmann"></div>
    </div>
    <div class="footer-band"><span>1820 Ridgeview Lane Denver, CO 80205 | <b>P:</b> 303-555-0140 | <b>F:</b> 303-555-0141</span></div>
  </section>

  <section class="envelope">
    <div class="flap">
      <div class="flap-band"></div>
      <div class="brand light"><span class="brand-square"></span><span>Feldberg<br>Formwerk</span></div>
      <div class="flap-tagline">EVERYTHING<br>W I L L &nbsp;B E<br>CUSTOM MADE</div>
      <div class="flap-url">www.feldberg-formwerk.at</div>
    </div>
    <div class="env-body">
      <div class="brand"><span class="brand-square"></span><span>Feldberg<br>Formwerk</span></div>
      <div class="ghost-name">FELDBERG</div>
      <div class="footer-band"><span>1820 Ridgeview Lane Denver, CO 80205 | <b>P:</b> 303-555-0140 | <b>F:</b> 303-555-0141</span></div>
    </div>
  </section>

  <section class="card card-front">
    <div class="brand light"><span class="brand-square"></span><span>Feldberg<br>Formwerk</span></div>
    <div class="card-tagline">EVERYTHING<br><span class="spaced">WILL BE</span><br>CUSTOM MADE</div>
    <div class="card-url">www.feldberg-formwerk.at</div>
  </section>

  <section class="card card-back">
    <div class="brand"><span class="brand-square"></span><span>Feldberg<br>Formwerk</span></div>
    <div class="card-person">
      <div class="name">Lena Hartmann</div>
      <div class="role">President</div>
      <div class="contact">lena.hartmann@feldberg-formwerk.at<br><b>M:</b> 01-555-0142</div>
    </div>
    <div class="footer-band"><span>1820 Ridgeview Lane Denver, CO 80205 | <b>P:</b> 303-555-0140 | <b>F:</b> 303-555-0141</span></div>
  </section>
</main>
</body>
</html>
```